Bright Owl Learning Centre website redesign

Our website (which we have only just converted to wordpress) is just not good enough for my liking. Our centre offers classes for babies aged from 6 months to 7 years old in the middle east. Whilst our program is formal in the way that the practise deals with learning in hemispheres of the brain - the site should look more fun and a bit more approachable and attractive to families.
I like the site www.tinyparade.example or www.plumvalley.example from this region - I like the way that you land on home page with images and a quote rather than all this information coming at you and you not knowing where to click.
I want a fun and appealing site that features info about the program, class timetable, shop, news and events, gallery, blog posts etc…
I am really open to a complete redesign and just want something that looks professional but is fun and gets the information out quickly! Please look at www.brightowl.example for current site design

```html
<!DOCTYPE html>
<html lang="en">
<head>
<meta charset="utf-8">
<title>Bright Owl Learning Centre</title>
<link href="https://fonts.googleapis.com/css2?family=Bree+Serif&family=Open+Sans:wght@400;600;700&family=Raleway:wght@500&family=Arimo:wght@400;700&display=swap" rel="stylesheet">
<style>
:root{
  --sky:#e6f3f9;
  --sky-top:#d4ebf5;
  --orange:#f7941d;
  --orange-dark:#f07a10;
  --teal:#3f87a8;
  --teal-dark:#216582;
  --navy:#2b5f86;
  --lime:#d7e36a;
  --lime-line:#f4f7c8;
  --text:#333;
  --muted:#555;
  --footer:#0f5a7a;
  --footer-deep:#0b4d6a;
  --footer-head:#7fd3ee;
  --white:#fff;
}
*{box-sizing:border-box;margin:0;padding:0}
html,body{width:961px;height:1200px;overflow:hidden}
body{position:relative;background:var(--sky);font-family:Arimo,Arial,sans-serif;color:var(--text)}
.abs{position:absolute}
.header-band{left:0;top:0;width:961px;height:125px;background:linear-gradient(#e9f5fa,var(--sky-top))}
.brand{left:86px;top:20px;width:80px;height:100px;display:flex;align-items:center;gap:6px;flex-direction:column;justify-content:center}
.brand-mark{width:34px;height:34px;border-radius:50%;background:var(--teal)}
.brand-name{font-family:'Open Sans',sans-serif;font-weight:700;font-size:11px;line-height:13px;color:var(--teal);text-align:center}
.call{right:88px;top:33px;font-family:'Open Sans',sans-serif;font-size:17px;color:#333;display:flex;align-items:center;gap:8px}
.call small{font-size:13px;color:var(--orange)}
.search{left:654px;top:70px;width:219px;height:25px;border:1px solid #e3b86c;border-radius:3px;background:linear-gradient(#fff,#fdf0d8);font-size:11px;color:#999;padding:6px 9px}
.search-btn{position:absolute;right:-1px;top:-1px;width:27px;height:25px;background:var(--orange);border-radius:0 3px 3px 0;display:flex;align-items:center;justify-content:center}
.nav{left:84px;top:133px;width:789px;height:33px;background:linear-gradient(#fba43a,var(--orange-dark));border-radius:3px;display:flex;align-items:center}
.nav a{font-family:'Open Sans',sans-serif;font-size:10.5px;color:#fff;text-decoration:none;letter-spacing:-.2px;position:absolute;top:10px}
.card{background:#fff;border-radius:4px;box-shadow:0 3px 0 #c9d8df}
.hero{left:85px;top:192px;width:549px;height:260px}
.hero-photo{left:8px;top:8px;width:534px;height:243px;background:linear-gradient(120deg,#c7a1a8,#e05a7a 45%,#f3c3cf 75%,#d9d3d6)}
.welcome{left:654px;top:192px;width:219px;height:260px;background:var(--lime);border-radius:6px;border:1px solid #c9d458}
.welcome-inner{position:absolute;inset:6px;border:1px dashed var(--lime-line);border-radius:4px;padding:14px 13px}
.welcome h2{font-family:'Bree Serif',serif;font-weight:400;font-size:18px;color:var(--navy);margin-bottom:10px}
.welcome p{font-size:10.6px;line-height:14.8px;color:#333}
.btn-orange{display:inline-block;margin-top:14px;background:var(--orange-dark);color:#fff;font-size:7.5px;font-weight:700;padding:6px 5px}
.box{top:478px;width:237px;height:232px}
.box-title{position:absolute;left:8px;top:10px;right:12px;height:27px;background:var(--teal);border-radius:6px;border-bottom:2px solid var(--teal-dark);font-family:'Open Sans',sans-serif;font-weight:600;font-size:13.5px;color:#fff;padding:4px 10px}
.star-photo{left:15px;top:50px;width:205px;height:82px;background:linear-gradient(90deg,#e7b59e,#d96e86 40%,#c9a0d9 70%,#eed2b8)}
.star-text{left:15px;top:140px;width:210px;font-size:9.2px;line-height:13.5px;color:#333}
.btn-dark{right:16px;top:200px;background:linear-gradient(#555,#222);color:#fff;font-size:9.5px;padding:4px 7px;border-radius:3px}
.event{position:absolute;left:15px;display:flex;gap:8px;width:215px}
.cal{flex:none;width:31px;height:32px;border:1.5px solid #c3202a;border-radius:3px;background:#fff;overflow:hidden;text-align:center}
.cal b{display:block;height:8px;background:#d22a33;color:#fff;font-size:4px;line-height:8px}
.cal span{font-family:'Arimo',sans-serif;font-weight:700;font-size:16px;line-height:22px}
.event p{font-size:8.8px;line-height:12px}
.event strong{font-size:9.3px}
.links{position:absolute;left:17px;top:58px;list-style:none}
.links li{font-family:'Open Sans',sans-serif;font-size:10.5px;color:#333;height:22.2px;display:flex;align-items:center;gap:6px}
.links li::before{content:"»";color:#8ab43a;font-size:9px}
.members-title{left:88px;top:745px;font-family:Raleway,sans-serif;font-weight:500;font-size:20px;color:var(--teal)}
.members-rule{left:88px;top:774px;width:460px;height:1px;background:#cfdfe7}
.pager{left:508px;top:751px;display:flex;gap:3px}
.pager i{width:13px;height:13px;border-radius:50%;background:#aaa;display:block}
.pager i+i{background:#777}
.post{left:90px;width:507px}
.post h3{font-size:9px;font-weight:700;color:#333}
.post em{display:block;font-size:9px;font-weight:700;color:var(--navy);margin:5px 0 13px}
.post p{font-size:9px;line-height:12.4px;color:#444}
.video{left:638px;top:759px;width:235px;height:171px;background:radial-gradient(circle at 50% 40%,#3a3a3a,#000 75%)}
.video-name{left:0;right:0;top:52px;text-align:center;font-family:'Open Sans',sans-serif;font-weight:700;font-size:11px;color:#9a9a9a}
.controls{left:4px;right:4px;bottom:4px;height:16px;background:linear-gradient(#eee,#bbb);border-radius:2px;font-size:7px;font-weight:700;display:flex;align-items:center;gap:5px;padding:0 5px}
.controls .bar{flex:1;height:3px;background:#888}
.footer{left:0;top:960px;width:961px;height:240px;background:linear-gradient(var(--footer),var(--footer-deep))}
.f-col h4{font-weight:400;font-size:12.5px;color:var(--footer-head);margin-bottom:14px}
.f-col{color:#fff;font-size:9.5px}
.contact-row{display:flex;gap:10px;align-items:center;margin-bottom:10px;line-height:15px}
.icon-circle{width:22px;height:22px;border-radius:50%;background:var(--orange-dark);display:flex;align-items:center;justify-content:center;flex:none}
.f-item{position:relative;padding-left:12px;color:#d2e5ee;font-size:8.8px;line-height:15px;margin-bottom:4px}
.f-item::before{content:"›";position:absolute;left:0;top:-2px;font-size:13px;color:#fff}
.f-item a{display:block;color:var(--orange);margin-top:4px;text-decoration:none}
.f-divider{width:1px;background:#3d7b97;top:983px;height:132px}
.f-rule{left:121px;top:1144px;width:713px;height:1px;background:#2f7594}
.f-links{left:121px;top:1163px;font-size:9px;color:#cfe6f0}
.social{top:1163px;width:26px;height:26px;border-radius:4px}
</style>
</head>
<body>
<div class="abs header-band"></div>

<div class="abs brand">
  <span class="brand-mark"></span>
  <span class="brand-name">Bright Owl<br>Learning Centre</span>
</div>

<div class="abs call">
  <svg width="16" height="14" viewBox="0 0 16 14"><path d="M3 11a6 6 0 0 1 0-8M6 9a3 3 0 0 1 0-4" stroke="#2b5f86" stroke-width="1.6" fill="none"/><circle cx="10" cy="7" r="2" fill="#2b5f86"/></svg>
  <small>Call Us Today</small> +00 (0)1200 34567
</div>

<div class="abs search">Search
  <span class="search-btn"><svg width="12" height="12" viewBox="0 0 12 12"><circle cx="5" cy="5" r="3.5" stroke="#5a3600" stroke-width="1.6" fill="none"/><path d="M7.6 7.6 11 11" stroke="#5a3600" stroke-width="2"/></svg></span>
</div>

<nav class="abs nav">
  <a style="left:16px">HOME</a>
  <a style="left:84px">THE PROGRAM</a>
  <a style="left:189px">CLASSES</a>
  <a style="left:286px">MEDIA</a>
  <a style="left:350px">OUR LOCATION</a>
  <a style="left:467px">BLOG</a>
  <a style="left:545px">ABOUT US</a>
  <a style="left:642px">SHOP</a>
  <a style="left:713px">CONTACT US</a>
</nav>

<section class="abs card hero">
  <div class="abs hero-photo" role="img" aria-label="Photo of a smiling baby in pink sitting among soft cushions"></div>
</section>

<aside class="abs welcome">
  <div class="welcome-inner">
    <h2>Welcome Message</h2>
    <p>The Bright Owl Learning Centre in Harbourside offers whole brain training for children from 6 months of age with the goal of promoting a balance in actively using both hemispheres whole brain training for children from 6 months of age with the goal of promoting a balance in actively using of the brain equally throughout life.</p>
    <span class="btn-orange">View Details »</span>
  </div>
</aside>

<section class="abs card box" style="left:85px">
  <div class="box-title">Star of the Month - Mira</div>
  <div class="abs star-photo" role="img" aria-label="Photo of young children reading a book together"></div>
  <p class="abs star-text">simply dummy text of the printing and typesetting industry. Lorem Ipsum has been the industry's standard the printing and typesetting industry.</p>
  <span class="abs btn-dark">More info</span>
</section>

<section class="abs card box" style="left:360px">
  <div class="box-title">News &amp; Events</div>
  <div class="event" style="top:52px"><div class="cal"><b>DECEMBER</b><span>31</span></div><p><strong>Lorem Ipsum is simply</strong><br>dummy text of the printing and typesetting industry. the printing</p></div>
  <div class="event" style="top:101px"><div class="cal"><b>DECEMBER</b><span>31</span></div><p><strong>Lorem Ipsum is simply</strong><br>dummy text of the printing and typesetting industry. the printing</p></div>
  <div class="event" style="top:149px"><div class="cal"><b>DECEMBER</b><span>31</span></div><p><strong>Lorem Ipsum is simply</strong><br>dummy text of the printing and typesetting industry. the printing</p></div>
</section>

<section class="abs card box" style="left:637px">
  <div class="box-title">More Information</div>
  <ul class="links">
    <li>Class Timetable</li>
    <li>Term Dates</li>
    <li>Bright Owl Program</li>
    <li>What is Whole Brain Training?</li>
    <li>The Team</li>
    <li>Our Location</li>
    <li>Contact Us</li>
  </ul>
</section>

<h2 class="abs members-title">Member’s Area</h2>
<div class="abs pager"><i></i><i></i></div>
<div class="abs members-rule"></div>

<article class="abs post" style="top:787px">
  <h3>Morbi adipiscing, augue et tincidunt vulputate, sapien mi facilisis turpis</h3>
  <em>Posted on : 12-02-13</em>
  <p>Aliquam et mauris mauris, et tempus tellus. Suspendisse placerat pretium nisi, nec pellentesque arcu vulputate at. Nulla gravida iaculis urna, eget eleifend odio malesuada non. Nulla facilisi.</p>
</article>
<article class="abs post" style="top:864px">
  <h3>Vestibulum egestas tincidunt sapien id vulputate. Nullam id orci turpis, eget varius lacus.</h3>
  <em>Posted on : 12-02-13</em>
  <p>Aliquam et mauris mauris, et tempus tellus. Suspendisse placerat pretium nisi, nec pellentesque arcu vulputate at. Nulla gravida iaculis urna, eget eleifend odio malesuada non. Nulla facilisi.</p>
</article>

<div class="abs video">
  <div class="abs video-name">Bright Owl<br>Learning Centre</div>
  <div class="abs controls">▶ <span>00:00</span><span class="bar"></span><span>00:00</span> ◂▮▮▮</div>
</div>

<footer class="abs footer"></footer>

<div class="abs f-col" style="left:124px;top:980px">
  <h4>Contact Us</h4>
  <div class="contact-row"><span class="icon-circle"><svg width="12" height="12" viewBox="0 0 12 12"><path d="M2 1l2.5 0 1 3-1.5 1a7 7 0 0 0 3 3l1-1.5 3 1V11A10 10 0 0 1 1 2z" fill="#fff"/></svg></span><span>+000 555 0101<br>+000 555 0102</span></div>
  <div class="contact-row"><span class="icon-circle"><svg width="12" height="9" viewBox="0 0 12 9"><rect x=".5" y=".5" width="11" height="8" fill="#fff"/><path d="M.5 .5 6 5l5.5-4.5" stroke="#f07a10" fill="none"/></svg></span><span>hello@brightowl.example<br>admin@brightowl.example</span></div>
  <div class="contact-row"><span class="icon-circle"><svg width="12" height="12" viewBox="0 0 12 12"><path d="M6 1 1 6h2v5h2.5V8h1v3H9V6h2z" fill="#fff"/></svg></span><span>12 Maple Lane,<br>Riverton, 00000</span></div>
</div>
<div class="abs f-divider" style="left:317px"></div>

<div class="abs f-col" style="left:372px;top:980px;width:220px">
  <h4>Latest Information</h4>
  <p class="f-item">Nullam rutrum est ac velit volutpat egestas eget sit amet mauris metus turpis, accumsan.<a>View more</a></p>
  <p class="f-item" style="margin-top:10px">Nullam rutrum est ac velit volutpat egestas eget sit amet mauris metus turpis, accumsan.<a>View more</a></p>
</div>
<div class="abs f-divider" style="left:637px"></div>

<div class="abs f-col" style="left:673px;top:980px;width:170px">
  <h4>Latest Discussions</h4>
  <p class="f-item">Mauris eget velit mauris, eget suscipit dui. Sed eget posuere elit.<a>Client Name</a></p>
  <p class="f-item" style="margin-top:10px">Mauris eget velit mauris, eget suscipit dui. Sed eget posuere elit.<a>Client Name</a></p>
</div>

<div class="abs f-rule"></div>
<div class="abs f-links">FAQ &nbsp;| &nbsp;Plans/Pricing &nbsp;| &nbsp;Contact &nbsp;| &nbsp;Login</div>
<span class="abs social" style="left:701px;background:#5cc8d8" role="img" aria-label="Social link"></span>
<span class="abs social" style="left:737px;background:#3b66b0" role="img" aria-label="Social link"></span>
<span class="abs social" style="left:773px;background:#f58220" role="img" aria-label="Social link"></span>
<span class="abs social" style="left:809px;background:#f46a1f" role="img" aria-label="Social link"></span>
</body>
</html>
```